Nobre Lente Lusitana - business card

Create a business card for my eyewear (glasses) store. The concept is based in handcrafted glasses (as well as common frames and 3d printed), clean, and elegant. The business card could be black (white letters and symbols) or white (black letters and symbols) but we are open to new suggestions. It must be sober and elegant.
The name Nobre Lente Lusitana means Royal/Real Portuguese Optical Store.
Our concept should be inspired by the pictures attatched bellow.
I would like it to be classic and elegant as business cards for bankers.
Our first selected logo is also available in attachment files.

Target Market(s)

For business meetings with investors, supliers and fairs

Industry/Entity Type

Eyewear

Contact Information for Business Card

Some random business cards in attachment that we like. Don't be closed to it, we like freedom of think.

Font styles to use
Serif
Sans Serif

Colors
404040
e9e9e9
fbfbfb
000000
85abd3
0255a3
f7fbfd
959595

Requirements
Must have
• Must be elegant, simple.
• Must present our brand new logo (slight variations are welcome, the logo is not closed yet). See our temporary logo in attachment.
• Black (or dark grey), white (or light grey) and a third slight color.
• This third slight color could be dark blue or grayish blue.
• Info:
• Tomás Vidigal (name)
• tvidigal@nobrelentelusitana.example
• +351 927364051
• www.nobrelentelusitana.example
Nice to have
• Black and white or with serious colors such as dark blue or greyish blue.
• Could also have water mark with our logo (big size) in the background (inspired in KMT bank credit card design)
Should not have
• Hysteric colora or shapes

```html
<!DOCTYPE html>
<html lang="pt">
<head>
<meta charset="utf-8">
<title>Nobre Lente Lusitana – Cartão de visita</title>
<link rel="stylesheet" href="https://fonts.googleapis.com/css2?family=Roboto+Slab:wght@700&family=Roboto+Condensed:wght@700&family=Roboto:wght@400&display=swap">
<style>
  :root {
    --stage: #3a3a3c;
    --brand-violet: #2e1b78;
    --paper: #f4f4f2;
    --ink: #404040;
    --rule: #6a6a6a;
    --on-violet: #ffffff;
  }
  * { margin: 0; padding: 0; box-sizing: border-box; }
  html, body {
    width: 1200px; height: 840px; overflow: hidden;
    background: var(--stage);
  }
  .stage {
    width: 1200px; height: 840px;
    display: flex; flex-direction: column;
    align-items: center; justify-content: center; gap: 60px;
  }
  .card {
    position: relative;
    width: 560px; height: 320px;
    overflow: hidden;
  }
  .card--front { background: var(--brand-violet); }
  .card--back { background: var(--paper); }

  .wordmark {
    font-family: "Roboto Slab", Georgia, serif;
    font-weight: 700;
    font-size: 20px;
    letter-spacing: 0.22em;
    text-transform: uppercase;
    white-space: nowrap;
  }
  .card--front .wordmark {
    position: absolute; left: 50%; top: 50%;
    transform: translate(-50%, -50%);
    color: var(--on-violet);
  }
  .card--back .wordmark {
    position: absolute; right: 40px; top: 70px;
    font-size: 15px;
    color: var(--brand-violet);
  }

  .rule-long {
    position: absolute; left: 36px; right: 36px; top: 178px;
    height: 1px; background: var(--rule);
  }
  .holder-name {
    position: absolute; left: 36px; top: 196px;
    font-family: "Roboto Condensed", "Arial Narrow", sans-serif;
    font-weight: 700; font-size: 21px;
    color: var(--brand-violet);
    text-transform: uppercase;
  }
  .rule-short {
    position: absolute; left: 36px; top: 232px;
    width: 150px; height: 1px; background: var(--rule);
  }
  .contact-list {
    position: absolute; left: 36px; top: 242px;
    list-style: none;
    font-family: "Roboto", Arial, sans-serif;
    font-size: 12.5px; color: var(--ink);
  }
  .contact-list li {
    display: flex; align-items: center; gap: 8px;
    height: 19px;
  }
  .contact-list svg { width: 11px; height: 11px; fill: var(--brand-violet); flex: none; }
</style>
</head>
<body>
<main class="stage">
  <section class="card card--front" aria-label="Frente do cartão">
    <p class="wordmark">Nobre Lente Lusitana</p>
  </section>

  <section class="card card--back" aria-label="Verso do cartão">
    <p class="wordmark">Nobre Lente Lusitana</p>
    <div class="rule-long"></div>
    <h1 class="holder-name">Tomás Vidigal</h1>
    <div class="rule-short"></div>
    <ul class="contact-list">
      <li>
        <svg viewBox="0 0 12 12" aria-hidden="true"><path d="M2.3 0.6l2 2.1-1 1.4c.7 1.6 2 2.9 3.6 3.6l1.4-1 2.1 2-1 2.2C5.6 11 1 6.4 0 1.6z"/></svg>
        <span>+351 927364051</span>
      </li>
      <li>
        <svg viewBox="0 0 12 12" aria-hidden="true"><path d="M0 2h12v1L6 7 0 3zM0 4.3l6 4 6-4V10H0z"/></svg>
        <span>tvidigal@nobrelentelusitana.example</span>
      </li>
      <li>
        <svg viewBox="0 0 12 12" aria-hidden="true"><circle cx="6" cy="6" r="6"/><path d="M0.5 6h11M6 0.5c-2.2 3-2.2 8 0 11M6 0.5c2.2 3 2.2 8 0 11" stroke="#f4f4f2" stroke-width="0.8" fill="none"/></svg>
        <span>www.nobrelentelusitana.example</span>
      </li>
    </ul>
  </section>
</main>
</body>
</html>
```